redesign laundry perfume webshop

We want to have a custom redesign for our website.
the focus should be luxury design . Please note that our "proefpakket" product is the most sold product.
Hello when desiging. please only use our product fotos, you can edit them, but dont make it look like there are other bottles etc.
Thank you for understanding.
Please dont show in english version (text). Use our language (dutch) use existing text on our website.
Also show our other pages as wel like category and product page etc.
Netherland and belgium
perfume
Coded - Design and coding required
5+ page
Designer to choose colors to be used in the design.

```html
<!DOCTYPE html>
<html lang="nl">
<head>
<meta charset="utf-8">
<title>Geurnest – Productpagina</title>
<link href="https://fonts.googleapis.com/css2?family=Barlow:wght@300;400;500;600&family=Libre+Baskerville:wght@400&family=Montserrat:wght@400;500&display=swap" rel="stylesheet">
<style>
:root{
  --board:#9a9a9a;
  --ink:#111111;
  --night:#1c1a1b;
  --paper:#f5f5f3;
  --white:#ffffff;
  --gold:#d7b244;
  --gold-deep:#c49a22;
  --gold-soft:#f6ecd2;
  --text:#3a3a3a;
  --muted:#8c8c8c;
  --line:#d9d9d9;
}
*{box-sizing:border-box;margin:0;padding:0}
html,body{width:1200px;height:2708px;overflow:hidden}
body{background:var(--board);font-family:"Barlow",sans-serif;color:var(--text);position:relative}
.abs{position:absolute}
.board-title{left:0;width:1200px;top:58px;text-align:center;color:var(--white);font-weight:300;font-size:76px;letter-spacing:2px;line-height:1}
.site{left:63px;top:191px;width:1062px;height:2433px;background:var(--paper);overflow:hidden}
/* header */
.topbar{left:0;top:0;width:1062px;height:59px;background:var(--ink);border-top:3px solid #3b4656}
.brand{left:105px;top:14px;display:flex;align-items:center;gap:8px;color:var(--gold);font-family:"Libre Baskerville",serif;font-size:22px}
.brand-dot{width:26px;height:26px;border-radius:50%;background:var(--gold)}
.nav a{position:absolute;top:21px;color:var(--white);font-family:"Montserrat",sans-serif;font-size:10px;letter-spacing:.6px;text-decoration:none}
.nav a.active{border-bottom:1.5px solid var(--gold);padding-bottom:5px}
.icons svg{position:absolute;top:20px}
/* hero */
.hero{left:0;top:59px;width:1062px;height:397px;background:linear-gradient(90deg,#e8c54f 0%,#ecc95a 38%,#c9b992 52%,#b9bcc0 70%,#d8d9d6 100%)}
.hero-kicker{left:0;width:518px;text-align:center;color:var(--white);font-weight:300;font-size:18px}
.hero-title{left:0;width:518px;text-align:center;color:var(--white);font-family:"Libre Baskerville",serif;font-weight:400;font-size:64px;line-height:1.2}
/* collection */
.eyebrow{color:var(--gold);font-size:14px;letter-spacing:1.2px;font-weight:400}
.section-title{font-family:"Libre Baskerville",serif;font-weight:400;font-size:29px;color:var(--ink)}
.rule{height:2px;background:var(--gold)}
.select{height:37px;display:flex;align-items:center;justify-content:space-between;padding:0 14px 0 18px;font-size:11.5px;letter-spacing:.5px}
.select.light{background:var(--white);border:1px solid var(--line);color:var(--text)}
.select.dark{background:var(--ink);color:var(--white)}
.card{width:201px;height:296px;background:var(--white);border:1px solid #ececec;text-align:center}
.card .name{position:absolute;left:0;width:100%;top:163px;font-family:"Libre Baskerville",serif;font-size:20px;color:var(--gold)}
.card .ship{position:absolute;left:0;width:100%;top:192px;font-size:10.5px;color:#555;letter-spacing:.3px}
.card .price{position:absolute;left:0;width:100%;top:214px;font-size:17px;color:var(--ink);letter-spacing:.5px}
.card .buy{position:absolute;left:43px;top:242px;width:115px;height:28px;border:1.5px solid var(--gold);font-size:9.5px;font-weight:600;letter-spacing:.6px;color:var(--ink);line-height:26px}
.product-shot{border-radius:10px 10px 4px 4px}
/* reviews */
.reviews{left:0;top:1478px;width:1062px;height:467px;background:var(--white)}
.review-card{left:233px;top:79px;width:592px;height:274px;background:var(--white);box-shadow:0 4px 18px rgba(0,0,0,.08);text-align:center}
.review-card .eyebrow{margin-top:44px;font-size:13px}
.review-title{margin-top:9px;font-family:"Libre Baskerville",serif;font-size:18px;color:var(--ink);text-transform:uppercase}
.review-text{margin:20px auto 0;width:490px;font-size:12.3px;line-height:18.5px;color:#444}
.author{left:233px;top:200px;display:flex;align-items:center;gap:10px;text-align:left}
.avatar{width:38px;height:38px;border-radius:50%;background:#b8a18a}
.author b{display:block;font-weight:500;font-size:13px;color:var(--ink)}
.author span{font-size:11px;color:var(--gold)}
/* newsletter + footer */
.newsletter{left:0;top:1945px;width:1062px;height:132px;background:var(--night);border-bottom:1px solid #333}
.news-title{left:114px;top:47px;font-family:"Libre Baskerville",serif;font-size:16px;color:var(--white);text-transform:uppercase}
.news-sub{left:114px;top:74px;width:290px;font-size:12.3px;line-height:14.5px;color:#bdbdbd}
.news-input{left:451px;top:55px;width:290px;height:37px;border:1px solid #8a8a8a;color:#bdbdbd;font-size:11px;padding:11px 18px}
.news-btn{left:747px;top:55px;width:146px;height:37px;background:linear-gradient(90deg,#e3c04c,#c99f2a);color:var(--white);font-size:11px;font-weight:600;text-align:center;line-height:37px;letter-spacing:.4px}
.footer{left:0;top:2077px;width:1062px;height:356px;background:var(--night)}
.foot-brand{left:128px;top:74px;width:130px;text-align:center}
.foot-mark{width:96px;height:96px;border-radius:50%;background:var(--gold);margin:0 auto 20px}
.foot-name{font-family:"Libre Baskerville",serif;font-size:20px;color:var(--gold)}
.col h4{font-weight:400;font-size:14px;letter-spacing:1.2px;color:var(--white)}
.col .rule{width:23px;height:1.5px;margin:5px 0 12px}
.col a{display:block;font-size:10.5px;color:#c9c9c9;text-decoration:none;line-height:20px}
.contact-row{display:flex;align-items:center;gap:10px;margin-bottom:17px;font-size:10.5px;color:#c9c9c9;line-height:15px}
.c-ico{width:25px;height:25px;border-radius:50%;background:var(--gold);display:flex;align-items:center;justify-content:center}
.socials{display:flex;gap:5px;margin-top:6px}
.socials i{width:25px;height:25px;border-radius:50%;background:var(--gold);display:block}
.foot-line{left:126px;top:294px;width:836px;height:1px;background:#3a3a3a}
.legal{top:313px;font-size:9.5px;color:#c9c9c9}
.legal.right{display:flex;gap:11px}
</style>
</head>
<body>
<div class="abs board-title">PRODUCT PAGE</div>

<div class="abs site">
  <header class="abs topbar">
    <div class="abs brand"><span class="brand-dot"></span>GEURNEST</div>
    <nav class="nav">
      <a class="active" style="left:400px">WASPARFUM</a>
      <a style="left:528px">CONTACT</a>
      <a style="left:625px">WAAROM GEURNEST</a>
    </nav>
    <div class="icons">
      <svg style="left:843px" width="17" height="17" viewBox="0 0 17 17" fill="none" stroke="#d7b244" stroke-width="1.5"><circle cx="7" cy="7" r="5.5"/><path d="M11 11l5 5"/></svg>
      <svg style="left:883px" width="18" height="18" viewBox="0 0 18 18" fill="none" stroke="#d7b244" stroke-width="1.5"><circle cx="9" cy="9" r="8"/><circle cx="9" cy="7.5" r="3"/><path d="M3.8 14.5c1.5-2 3.2-3 5.2-3s3.7 1 5.2 3"/></svg>
      <svg style="left:922px" width="18" height="17" viewBox="0 0 18 17" fill="none" stroke="#d7b244" stroke-width="1.5"><path d="M2 5h14l-1 11H3z"/><path d="M6 5V3.5a3 3 0 0 1 6 0V5"/></svg>
    </div>
  </header>

  <section class="abs hero" role="img" aria-label="Foto: vrouw ruikt aan frisse handdoek bij wasmachine, gouden achtergrond links"></section>
  <div class="abs hero-kicker" style="top:192px">Muffewas is nu verleden Tijd!</div>
  <div class="abs hero-title" style="top:212px">Geurnest</div>

  <div class="abs eyebrow" style="left:111px;top:520px">ONZE COLLECTIE</div>
  <h2 class="abs section-title" style="left:112px;top:539px">Onze Producten</h2>
  <div class="abs rule" style="left:112px;top:584px;width:74px"></div>
  <div class="abs select light" style="left:715px;top:546px;width:117px">FILTEREN
    <svg width="10" height="6" viewBox="0 0 10 6" fill="none" stroke="#111" stroke-width="1.4"><path d="M1 1l4 4 4-4"/></svg></div>
  <div class="abs select dark" style="left:840px;top:546px;width:115px">SORTEREN
    <svg width="10" height="6" viewBox="0 0 10 6" fill="none" stroke="#fff" stroke-width="1.4"><path d="M1 1l4 4 4-4"/></svg></div>

  <!-- row 1 -->
  <div class="abs card" style="left:108px;top:705px"><div class="name">Zomerregen</div><div class="ship">voor 16:00 besteld = vandaag</div><div class="price">14.95</div><div class="buy">IN WINKELMAND</div></div>
  <div class="abs card" style="left:324px;top:705px"><div class="name">Zomerregen</div><div class="ship">voor 16:00 besteld = vandaag</div><div class="price">14.95</div><div class="buy">IN WINKELMAND</div></div>
  <div class="abs card" style="left:541px;top:705px"><div class="name">Zomerregen</div><div class="ship">voor 16:00 besteld = vandaag</div><div class="price">14.95</div><div class="buy">IN WINKELMAND</div></div>
  <div class="abs card" style="left:756px;top:705px"><div class="name">Zomerregen</div><div class="ship">voor 16:00 besteld = vandaag</div><div class="price">14.95</div><div class="buy">IN WINKELMAND</div></div>
  <div class="abs product-shot" style="left:166px;top:648px;width:85px;height:201px;background:linear-gradient(180deg,#f4f4f4 0 22%,#d7e8f6 22%,#a9cdea 100%)" role="img" aria-label="Productfoto: fles wasparfum met lichtblauw etiket"></div>
  <div class="abs product-shot" style="left:383px;top:644px;width:85px;height:205px;background:linear-gradient(180deg,#f4f4f4 0 22%,#e6a0a2 22%,#b7222b 100%)" role="img" aria-label="Productfoto: fles wasparfum met rood etiket"></div>
  <div class="abs product-shot" style="left:600px;top:646px;width:85px;height:203px;background:linear-gradient(180deg,#f4f4f4 0 22%,#e6f0f9 22%,#9fc6ea 100%)" role="img" aria-label="Productfoto: fles wasparfum met wit-blauw etiket"></div>
  <div class="abs product-shot" style="left:815px;top:648px;width:85px;height:203px;background:linear-gradient(180deg,#f4f4f4 0 22%,#4d4d8e 22%,#21226a 100%)" role="img" aria-label="Productfoto: fles wasparfum met donkerblauw etiket"></div>

  <!-- row 2 -->
  <div class="abs card" style="left:110px;top:1077px"><div class="name">Zomerregen</div><div class="ship">voor 16:00 besteld = vandaag</div><div class="price">14.95</div><div class="buy">IN WINKELMAND</div></div>
  <div class="abs card" style="left:326px;top:1077px"><div class="name">Zomerregen</div><div class="ship">voor 16:00 besteld = vandaag</div><div class="price">14.95</div><div class="buy">IN WINKELMAND</div></div>
  <div class="abs card" style="left:543px;top:1077px"><div class="name">Zomerregen</div><div class="ship">voor 16:00 besteld = vandaag</div><div class="price">14.95</div><div class="buy">IN WINKELMAND</div></div>
  <div class="abs card" style="left:758px;top:1077px"><div class="name">Zomerregen</div><div class="ship">voor 16:00 besteld = vandaag</div><div class="price">14.95</div><div class="buy">IN WINKELMAND</div></div>
  <div class="abs product-shot" style="left:172px;top:1028px;width:79px;height:197px;background:linear-gradient(180deg,#f4f4f4 0 20%,#5a2f16 20% 38%,#f7f3ea 38% 92%,#3b2415 92%)" role="img" aria-label="Productfoto: flesje geurolie met wit etiket"></div>
  <div class="abs" style="left:352px;top:1122px;width:154px;height:82px;background:linear-gradient(180deg,#2a1a10 0 30%,#d78a2a 30%,#f0c26a 70%,#8a4b16 100%)" role="img" aria-label="Productfoto: proefpakket met vijf flesjes in geschenkdoos"></div>
  <div class="abs product-shot" style="left:603px;top:1027px;width:82px;height:199px;background:linear-gradient(180deg,#f4f4f4 0 22%,#f6b23a 22%,#e88a0c 100%)" role="img" aria-label="Productfoto: fles wasparfum met oranje etiket"></div>
  <div class="abs product-shot" style="left:818px;top:1027px;width:79px;height:197px;background:linear-gradient(180deg,#f4f4f4 0 20%,#5a2f16 20% 38%,#f7f3ea 38% 92%,#2a1d12 92%)" role="img" aria-label="Productfoto: flesje geurolie met wit etiket"></div>

  <!-- reviews -->
  <section class="abs reviews">
    <div class="abs" style="left:749px;top:44px;width:106px;height:106px;border-radius:50%;background:linear-gradient(135deg,#e7c552,#b98f1e)"></div>
    <div class="abs" style="left:192px;top:256px;width:106px;height:106px;border-radius:50%;background:var(--gold-soft)"></div>
    <div class="abs review-card">
      <div class="eyebrow">BEOORDELINGEN</div>
      <div class="review-title">Onze blije klanten aan het woord</div>
      <p class="review-text">Wat ben ik gelukkig met deze geurtjes! Mijn vriend en ik zijn heel gevoelig als het op geur aankomt. Wij worden snel onpasselijk van luchtjes, maar als het de juiste zijn worden wij heel blij. Wat ben ik blij dat ik jullie ontdekt heb. Ik ben nog met het proefpakket bezig, maar ik weet nu al dat ik dit voortaan ga gebruiken. Echt zo lekker!</p>
      <div class="abs author"><div class="avatar" role="img" aria-label="Profielfoto van de klant"></div><div><b>Lotte Maas</b><span>Klant ervaring online</span></div></div>
    </div>
    <svg class="abs" style="left:135px;top:213px" width="24" height="16" viewBox="0 0 24 16" fill="none" stroke="#444" stroke-width="1.4"><path d="M23 8H2M8 1L1 8l7 7"/></svg>
    <svg class="abs" style="left:886px;top:213px" width="24" height="16" viewBox="0 0 24 16" fill="none" stroke="#444" stroke-width="1.4"><path d="M1 8h21M16 1l7 7-7 7"/></svg>
  </section>

  <!-- newsletter -->
  <section class="abs newsletter">
    <div class="abs news-title">Aanmelden voor nieuwsbrief?</div>
    <div class="abs news-sub">U wordt maandelijks op de hoogte gehouden van kortingen en nieuwste producten!</div>
    <div class="abs news-input">Emailadres</div>
    <div class="abs news-btn">AANMELDEN</div>
  </section>

  <footer class="abs footer">
    <div class="abs foot-brand"><div class="foot-mark"></div><div class="foot-name">GEURNEST</div></div>
    <div class="abs col" style="left:339px;top:43px">
      <h4>INFORMATIE</h4><div class="rule"></div>
      <a>Veel gestelde vragen</a><a>Klantenervaring</a><a>Betaalmogelijkheden</a><a>Verzenden en retourneren</a>
    </div>
    <div class="abs col" style="left:546px;top:43px">
      <h4>SNELLE LINKS</h4><div class="rule"></div>
      <a>Wasparfum proefpakket</a><a>Verkooppunten</a><a>Verkooppunt worden?</a><a>Blogs</a><a>contact ons</a><a>Algemene voorwaarden</a><a>Onze Wasparfums</a>
    </div>
    <div class="abs col" style="left:748px;top:43px">
      <h4>CONTACT</h4><div class="rule"></div>
      <div class="contact-row"><span class="c-ico"><svg width="12" height="12" viewBox="0 0 12 12" fill="#1c1a1b"><path d="M2.5 1l2 2.2-1 1.3c.8 1.6 2 2.8 3.9 3.9l1.3-1 2.3 2-1 1.6C5.5 11 1 6.5 1 2z"/></svg></span><div>Telefoonnummer<br>+31205550147</div></div>
      <div class="contact-row"><span class="c-ico"><svg width="12" height="9" viewBox="0 0 12 9" fill="none" stroke="#1c1a1b" stroke-width="1.3"><rect x=".7" y=".7" width="10.6" height="7.6"/><path d="M1 1l5 4 5-4"/></svg></span><div>Mail ons<br>info@geurnest.nl</div></div>
      <div class="socials"><i></i><i></i><i></i><i></i></div>
    </div>
    <div class="abs foot-line"></div>
    <div class="abs legal" style="left:132px">Alle rechten voorbehouden © 2023 Geurnest</div>
    <div class="abs legal right" style="left:734px"><span>Privacybeleid</span><span>Algemene voorwaarden</span><span>Sitemap</span></div>
  </footer>
</div>
</body>
</html>
```